We would like to have one website and the similar (or the same) Facebook site.
We need only the first website without sub-pages and menus. We are preparing a new product for the market. On the page should be the logo, company data, few pictures and the text about our product.
The company color is red.
Company data are Ventrolo GmbH, CH-7342 Uster, Switzerland, media@ventrolo.com, www.ventrolo.com.
Text for the page:
"We are Swiss engineers with many years of experience in ultra-precision electronics.
We develop the Nordelix, a smartwatch that can save lives. It is designed for elderly people who live alone and want to maintain their independence longer, without fear.
Our Nordelix will be available at 4th quarter of 2018."

```html
<!DOCTYPE html>
<html lang="en">
<head>
<meta charset="utf-8">
<title>Ventrolo – Nordelix</title>
<link href="https://fonts.googleapis.com/css2?family=Roboto:wght@400;500;700&family=Mulish:wght@400;600;700&display=swap" rel="stylesheet">
<style>
:root{
  --red:#e21f26;
  --ink:#333333;
  --muted:#666666;
  --light:#eeeeee;
  --white:#ffffff;
  --line:#d9d9d9;
}
*{margin:0;padding:0;box-sizing:border-box}
html,body{width:1200px;height:3327px;overflow:hidden;background:var(--white)}
body{position:relative;font-family:"Mulish",sans-serif;color:var(--ink)}
section,header,footer{position:absolute;left:0;width:1200px;overflow:hidden}

/* header */
.site-header{top:0;height:93px;background:var(--white)}
.brand{position:absolute;left:126px;top:20px;font-family:"Roboto",sans-serif;font-weight:700;font-size:48px;color:var(--red);letter-spacing:-0.5px;line-height:1}
.header-tag{position:absolute;right:126px;top:36px;font-size:16px;color:var(--muted)}

/* hero */
.hero{top:93px;height:550px}
.hero-photo{position:absolute;inset:0;background:linear-gradient(90deg,#8d8a86 0%,#b4aca3 45%,#d8d1c7 75%,#c9c3bb 100%)}
.hero-title{position:absolute;left:122px;top:188px;font-family:"Roboto",sans-serif;font-weight:500;font-size:38px;line-height:48px;color:var(--white)}
.btn{position:absolute;display:flex;align-items:center;justify-content:center;font-size:14px;font-weight:600;text-transform:uppercase;letter-spacing:.3px;text-decoration:none}
.btn-red{background:var(--red);color:var(--white)}
.hero .btn{left:124px;top:306px;width:189px;height:45px}
.dots{position:absolute;left:555px;top:504px;display:flex;gap:9px}
.dots span{width:13px;height:13px;border-radius:50%;background:var(--white)}
.dots span:first-child{background:transparent;border:2px solid var(--white)}

/* about */
.about{top:643px;height:459px;background:var(--white)}
.watch-img{position:absolute;border-radius:40px;background:radial-gradient(circle at 45% 45%,#5b5b5b 0%,#222 60%,#111 100%)}
.about .watch-img{left:130px;top:80px;width:450px;height:300px}
.section-title{font-family:"Roboto",sans-serif;font-weight:400;color:var(--ink)}
.section-title em{font-style:normal;color:var(--red)}
.about .section-title{position:absolute;left:632px;top:75px;font-size:36px}
.about .copy{position:absolute;left:632px;top:133px;width:440px;font-size:14px;line-height:22px;color:var(--muted)}
.about .copy p+p{margin-top:14px}
.btn-grey{background:linear-gradient(#8a8a8a,#6c6c6c);color:var(--white)}
.about .btn{left:639px;top:317px;width:164px;height:47px}

/* benefits */
.benefits{top:1102px;height:579px;background:var(--red)}
.notch{position:absolute;left:569px;top:0}
.benefits h2{position:absolute;left:0;width:1200px;top:45px;text-align:center;font-family:"Roboto",sans-serif;font-weight:400;font-size:29px;color:var(--white)}
.benefits .rule{position:absolute;left:570px;top:88px;width:60px;height:2px;background:var(--white)}
.benefits .watch-img{left:472px;top:135px;width:258px;height:400px;border-radius:60px}
.feature{position:absolute;width:340px}
.feature h3{font-family:"Roboto",sans-serif;font-weight:500;font-size:16px;color:var(--white);margin-bottom:6px}
.feature p{font-size:11px;line-height:15px;color:rgba(255,255,255,.85)}
.feature.left{text-align:right}
.feature .icon{position:absolute;top:-4px;width:64px;height:64px;border-radius:50%;background:#8a8a8a;border:3px solid var(--white);display:flex;align-items:center;justify-content:center}
.feature.left .icon{right:-83px}
.feature.right .icon{left:-79px}

/* help */
.help{top:1681px;height:499px;background:var(--light)}
.help-photo{position:absolute;left:444px;top:0;width:756px;height:499px;background:linear-gradient(90deg,#ebe9e6 0%,#d9cdc0 30%,#c9b9a6 60%,#e6e4dc 100%)}
.help h2{position:absolute;left:122px;top:97px;font-family:"Roboto",sans-serif;font-weight:400;font-size:34px;color:var(--ink)}
.help .copy{position:absolute;left:122px;top:152px;width:400px;font-size:15px;line-height:24px;color:var(--muted)}
.help .copy p+p{margin-top:10px}
.btn-outline-red{border:2px solid var(--red);color:var(--red);background:transparent}
.help .btn{left:124px;top:309px;width:173px;height:45px}

/* testimonial */
.testimonial{top:2180px;height:393px;background:linear-gradient(90deg,#2f2f2f 0%,#4a4542 50%,#3a3634 100%)}
.play{position:absolute;left:560px;top:99px}
.quote{position:absolute;left:0;width:1200px;top:170px;text-align:center;font-size:22px;line-height:38px;color:var(--white)}
.quote .mark{font-size:30px;vertical-align:top;line-height:30px}
.avatars{position:absolute;left:501px;top:264px;display:flex;gap:8px}
.avatars span{width:40px;height:40px;border-radius:50%;border:2px solid var(--white)}

/* order */
.order{top:2573px;height:399px;background:linear-gradient(110deg,#2b2b2b 0%,#3f3f3f 35%,#b3242a 60%,var(--red) 80%)}
.order .watch-img{left:190px;top:40px;width:290px;height:330px;border-radius:60px}
.order h2{position:absolute;left:570px;top:86px;font-family:"Roboto",sans-serif;font-weight:400;font-size:34px;color:var(--white)}
.order .lead{position:absolute;left:570px;top:130px;font-size:17px;color:var(--white)}
.order .copy{position:absolute;left:570px;top:168px;width:480px;font-size:12px;line-height:20px;color:rgba(255,255,255,.9)}
.btn-outline-white{border:2px solid var(--white);color:var(--white)}
.order .btn{left:572px;top:255px;width:164px;height:44px}

/* footer */
.site-footer{top:2972px;height:355px;background:var(--white)}
.site-footer .brand{left:115px;top:80px;font-size:50px}
.fcol{position:absolute;top:76px}
.fcol h4{font-family:"Roboto",sans-serif;font-weight:500;font-size:20px;color:var(--ink);margin-bottom:16px}
.fcol p{font-size:14px;line-height:31px;color:var(--muted)}
.social{display:flex;gap:7px;margin-top:4px}
.social span{width:40px;height:40px;border-radius:50%;border:2px solid var(--red)}
.footer-rule{position:absolute;left:106px;top:284px;width:977px;height:1px;background:var(--line)}
.copyright{position:absolute;left:0;width:1200px;top:313px;text-align:center;font-size:12px;color:var(--muted)}
</style>
</head>
<body>

<header class="site-header">
  <div class="brand">Ventrolo</div>
  <p class="header-tag">Swiss ultra-precision electronics</p>
</header>

<section class="hero">
  <div class="hero-photo" role="img" aria-label="Photo of an elderly man and a smiling young woman at home"></div>
  <h1 class="hero-title">Smartwatch that can Save<br>Live of Elderly People</h1>
  <a class="btn btn-red" href="#">View our watch</a>
  <div class="dots"><span></span><span></span><span></span><span></span></div>
</section>

<section class="about">
  <div class="watch-img" role="img" aria-label="Product photo of two black Nordelix smartwatches"></div>
  <h2 class="section-title">About <em>Nordelix</em></h2>
  <div class="copy">
    <p>We are Swiss engineers with many years of experience in ultra-precision electronics.</p>
    <p>We develop the Nordelix, a smartwatch that can save lives. It is designed for elderly people who live alone and want to maintain their independence longer, without fear.</p>
  </div>
  <a class="btn btn-grey" href="#">Learn more</a>
</section>

<section class="benefits">
  <svg class="notch" width="62" height="20" viewBox="0 0 62 20"><path d="M0 0 H62 L31 20 Z" fill="#ffffff"/></svg>
  <h2>Benefits &amp; Features</h2>
  <div class="rule"></div>
  <div class="watch-img" role="img" aria-label="Product photo of a black Nordelix smartwatch with red button"></div>

  <div class="feature left" style="left:37px;top:145px">
    <h3>Help Senior Citizens</h3><p>Keeps seniors independent<br>longer and without fear</p>
    <div class="icon"><svg width="30" height="30" viewBox="0 0 30 30" fill="#fff"><circle cx="15" cy="6" r="4"/><path d="M10 12 h10 v9 h-3 v7 h-4 v-7 h-3z"/></svg></div>
  </div>
  <div class="feature left" style="left:37px;top:281px">
    <h3>Voice Calling</h3><p>Talk to family right from<br>the watch on your wrist</p>
    <div class="icon"><svg width="28" height="28" viewBox="0 0 24 24" fill="#fff"><path d="M6.6 10.8a15 15 0 0 0 6.6 6.6l2.2-2.2c.3-.3.7-.4 1-.2 1.1.4 2.3.6 3.6.6.6 0 1 .4 1 1V20c0 .6-.4 1-1 1A17 17 0 0 1 3 4c0-.6.4-1 1-1h3.5c.6 0 1 .4 1 1 0 1.3.2 2.5.6 3.6.1.3 0 .7-.2 1z"/></svg></div>
  </div>
  <div class="feature left" style="left:37px;top:416px">
    <h3>Easy to Use</h3><p>Simple screen and one big<br>button for every situation</p>
    <div class="icon"><svg width="28" height="28" viewBox="0 0 24 24"><circle cx="12" cy="12" r="7" fill="none" stroke="#fff" stroke-width="4" stroke-dasharray="3 2.5"/><circle cx="12" cy="12" r="3" fill="#fff"/></svg></div>
  </div>

  <div class="feature right" style="left:821px;top:145px">
    <h3>Health Emergency</h3><p>Call for help with a single<br>press when it matters</p>
    <div class="icon"><svg width="28" height="28" viewBox="0 0 24 24" fill="#fff"><path d="M9 3h6v6h6v6h-6v6H9v-6H3V9h6z"/></svg></div>
  </div>
  <div class="feature right" style="left:821px;top:281px">
    <h3>Smart Locator</h3><p>Shows where help is needed<br>at home or outside</p>
    <div class="icon"><svg width="26" height="30" viewBox="0 0 24 28" fill="#fff"><path d="M12 1a8 8 0 0 0-8 8c0 6 8 17 8 17s8-11 8-17a8 8 0 0 0-8-8zm0 11a3 3 0 1 1 0-6 3 3 0 0 1 0 6z"/></svg></div>
  </div>
  <div class="feature right" style="left:821px;top:416px">
    <h3>Live alone is Easy</h3><p>Made for elderly people<br>who live on their own</p>
    <div class="icon"><svg width="30" height="30" viewBox="0 0 24 24" fill="#fff"><path d="M12 3a9 9 0 0 0-9 9h18a9 9 0 0 0-9-9z"/><path d="M11.2 12h1.6v7a2.3 2.3 0 0 1-4.6 0h1.6a.7.7 0 0 0 1.4 0z"/></svg></div>
  </div>
</section>

<section class="help">
  <div class="help-photo" role="img" aria-label="Photo of an elderly mother embraced by her smiling adult daughter"></div>
  <h2>Help Your Elderly Parents</h2>
  <div class="copy">
    <p>Nordelix is designed for elderly people who live alone and want to maintain their independence longer.</p>
    <p>A smartwatch that can save lives, worn every day without fear.</p>
  </div>
  <a class="btn btn-outline-red" href="#">Learn more</a>
</section>

<section class="testimonial" role="img" aria-label="Darkened photo of two women in the background">
  <svg class="play" width="56" height="56" viewBox="0 0 56 56"><circle cx="28" cy="28" r="26" fill="none" stroke="#fff" stroke-width="3"/><path d="M22 17 L39 28 L22 39 Z" fill="#fff"/></svg>
  <p class="quote"><span class="mark">“</span>We develop the Nordelix, a smartwatch that can save lives<br>for elderly people who want to live alone without fear<span class="mark">”</span></p>
  <div class="avatars">
    <span style="background:#e0675a" role="img" aria-label="Customer portrait"></span>
    <span style="background:#9a9a9a" role="img" aria-label="Customer portrait"></span>
    <span style="background:#8c8c8c" role="img" aria-label="Customer portrait"></span>
    <span style="background:#a5a5a5" role="img" aria-label="Customer portrait"></span>
  </div>
</section>

<section class="order">
  <div class="watch-img" role="img" aria-label="Product photo of the Nordelix smartwatch showing a help prompt"></div>
  <h2>Order Watch Now</h2>
  <p class="lead">Our Nordelix will be available at 4th quarter of 2018</p>
  <p class="copy">Developed by Swiss engineers at Ventrolo GmbH, CH-7342 Uster, Switzerland. Write to media@ventrolo.com to be among the first to receive your Nordelix smartwatch.</p>
  <a class="btn btn-outline-white" href="#">Click here</a>
</section>

<footer class="site-footer">
  <div class="brand">Ventrolo</div>
  <div class="fcol" style="left:381px"><h4>Company</h4><p>Ventrolo GmbH</p><p>CH-7342 Uster</p><p>Switzerland</p></div>
  <div class="fcol" style="left:580px"><h4>Contact</h4><p>media@ventrolo.com</p><p>www.ventrolo.com</p></div>
  <div class="fcol" style="left:780px"><h4>Product</h4><p>Nordelix</p><p>Q4 2018</p></div>
  <div class="fcol" style="left:912px"><h4>Stay in Touch</h4>
    <div class="social"><span aria-label="Social link"></span><span aria-label="Social link"></span><span aria-label="Social link"></span><span aria-label="Social link"></span></div>
  </div>
  <div class="footer-rule"></div>
  <p class="copyright">© 2018 Ventrolo GmbH&nbsp; All rights reserved&nbsp; www.ventrolo.com</p>
</footer>

</body>
</html>
```